5.5 x 8.5 two sided marketing brochure

//Some great entries already. Please note that we would like the offer (either Risk Free Testing Resource OR Free Proof of Concept) to be more popping out! And it's either one or the other, it's not one offer

We are looking to have this done in the next 12 hours. A portrait (width 5x5 inches, height 8.5 inches) .eps or .ai format two sided brochure.

Our client focuses on 2 things: outsourced testing resources and a platform that automates testing for web, mobile, desktop and APIs.

They are looking for a much bolder design (except for their logo, it should stay as is).
You can find content and info on the business here: velocity brightlane dot com (remove all spaces, replace dot with .).

First page should focus on 2 offers and 1 case study.
Offer is: Risk free testing resource OR
Receive a test automation proof of concept for web, mobile, desktop, or API app.
Case study is among the lines of: see how Qorvel Inc is automating thousands of test cases using the platform, and saving thousands of dollars in license fees.

Small print legal info at the bottom of the page. For now, just do about 60 words lorem ipsum.

Second page should be all about the company: profile and what they do.
This should focus on resource outsourcing, their automation testing platform, and customer logos.

We really like how beautiful the design of the attached document is (focus on page 2) and it obviously should be 5.5x8.5 inches

```html
<!DOCTYPE html>
<html lang="en">
<head>
<meta charset="utf-8">
<title>Velocity Brightlane – Two-Sided Brochure</title>
<link rel="stylesheet" href="https://fonts.googleapis.com/css2?family=Lato:wght@400;700;900&display=swap">
<style>
  :root {
    --teal: #1fb0bb;
    --teal-dark: #15939d;
    --teal-pale: #d9f4f6;
    --ink: #333a3f;
    --ink-soft: #5c6368;
    --rule: #c9cdd0;
    --paper: #ffffff;
    --backdrop: #f4f5f6;
    --photo-dark: #2c3338;
    --photo-mid: #59636a;
  }
  * { box-sizing: border-box; margin: 0; padding: 0; }
  html, body { width: 1200px; height: 991px; overflow: hidden; }
  body {
    background: var(--backdrop);
    font-family: "Lato", Arial, sans-serif;
    color: var(--ink);
    position: relative;
  }
  .page {
    position: absolute;
    background: var(--paper);
    overflow: hidden;
  }
  .abs { position: absolute; }

  /* ---------- Front page ---------- */
  .front { left: 107px; top: 171px; width: 433px; height: 636px; }
  .brand {
    left: 16px; top: 8px;
    display: flex; align-items: center; gap: 8px;
  }
  .brand-dot {
    width: 26px; height: 26px; border-radius: 50%;
    background: var(--teal);
  }
  .brand-name {
    font-size: 13px; line-height: 14px; font-weight: 400;
    letter-spacing: 1.5px; color: var(--teal);
    text-transform: uppercase;
  }
  .hero-art { left: 0; top: 0; width: 433px; height: 325px; }
  .hero-title {
    left: 30px; top: 150px;
    font-size: 34px; font-weight: 900; color: #fff; letter-spacing: 0.5px;
  }
  .hero-text {
    left: 30px; top: 200px; width: 300px;
    font-size: 14.5px; line-height: 17px; color: var(--teal-pale);
  }
  .rule {
    height: 2px; background: var(--rule);
  }
  .rule::before {
    content: ""; position: absolute; left: 0; top: 0;
    width: 30px; height: 2px; background: var(--teal);
  }
  .offer-copy {
    width: 176px;
    font-size: 14px; line-height: 18px; color: var(--ink);
    text-align: justify; hyphens: auto;
  }
  .offer-title {
    left: 224px; top: 360px;
    font-size: 20px; font-weight: 900; color: var(--teal);
  }
  .offer-list { left: 222px; top: 407px; list-style: none; }
  .offer-list li {
    display: flex; align-items: center; gap: 10px;
    font-size: 13.5px; color: var(--ink); height: 40px;
  }
  .offer-list svg { width: 22px; height: 22px; flex: none; }
  .legal {
    left: 27px; top: 590px; width: 376px;
    font-size: 5.6px; line-height: 7px; color: var(--ink-soft);
  }

  /* ---------- Back page ---------- */
  .back { left: 633px; top: 140px; width: 433px; height: 667px; }
  .sq { background: var(--teal); }
  .profile-title {
    left: 20px; top: 146px;
    font-size: 29px; line-height: 31px; font-weight: 900;
    color: var(--teal); letter-spacing: 0.3px;
  }
  .profile-text {
    left: 20px; top: 222px; width: 190px;
    font-size: 13px; line-height: 19px; color: var(--ink-soft);
  }
  .facts { left: 240px; top: 32px; width: 180px; }
  .fact-head {
    font-size: 10px; font-weight: 900; color: var(--ink);
    text-transform: uppercase; margin-bottom: 5px;
  }
  .fact-head span, .section-head span { color: var(--teal); }
  .fact-text {
    font-size: 8.2px; line-height: 12px; color: var(--ink-soft);
    margin-bottom: 12px;
  }
  .section-head {
    left: 0; width: 433px; text-align: center;
    font-size: 10px; font-weight: 700; color: var(--ink);
    text-transform: uppercase;
  }
  .stats { left: 40px; top: 392px; width: 353px; display: flex; justify-content: space-between; }
  .stat { width: 80px; text-align: center; }
  .stat svg { width: 40px; height: 40px; display: block; margin: 0 auto; }
  .stat-num { font-size: 18px; color: var(--ink); margin-top: 6px; }
  .stat-bar { width: 26px; height: 2px; background: var(--teal); margin: 6px auto 8px; }
  .stat-label { font-size: 8.5px; line-height: 11px; color: var(--ink); text-transform: uppercase; }
  .clients {
    left: 28px; top: 574px; width: 377px;
    display: flex; justify-content: space-between; align-items: center;
  }
  .client { display: flex; align-items: center; gap: 3px; font-size: 7.5px; font-weight: 700; color: var(--ink); }
  .client i { width: 8px; height: 8px; background: var(--teal); display: block; }
  .contact-band {
    left: 0; top: 629px; width: 433px; height: 38px;
    background: var(--teal); color: #fff;
    display: flex; align-items: center; font-size: 9px;
  }
  .contact-item { position: absolute; display: flex; align-items: center; gap: 10px; }
  .contact-item svg { width: 14px; height: 14px; }
</style>
</head>
<body>

<!-- Front page -->
<section class="page front">
  <svg class="abs hero-art" viewBox="0 0 433 325" aria-hidden="false">
    <defs>
      <linearGradient id="photoTone" x1="0" y1="0" x2="1" y2="1">
        <stop offset="0" stop-color="#6f7b80"/>
        <stop offset="0.5" stop-color="#2c3338"/>
        <stop offset="1" stop-color="#8a9297"/>
      </linearGradient>
    </defs>
    <rect x="150" y="0" width="283" height="325" fill="url(#photoTone)" role="img" aria-label="Photo of hands typing on a laptop showing a test automation dashboard"/>
    <polygon points="0,105 372,105 345,325 0,325" fill="var(--teal)" opacity="0.96"/>
  </svg>
  <div class="abs brand">
    <span class="brand-dot"></span>
    <span class="brand-name">Velocity<br>Brightlane</span>
  </div>
  <h1 class="abs hero-title">MEET ZEPHRA</h1>
  <p class="abs hero-text">is ALL-IN-ONE test automation tool that empowers testers and developers to easily create, run, and manage continuous delivery and testing cycles</p>

  <div class="abs rule" style="left:27px; top:347px; width:176px;"></div>
  <div class="abs rule" style="left:224px; top:347px; width:176px;"></div>

  <p class="abs offer-copy" style="left:27px; top:360px;">Risk free testing resource or receive a test automation proof of concept for web, mobile, desktop, or API app.</p>
  <div class="abs rule" style="left:27px; top:447px; width:176px;"></div>
  <p class="abs offer-copy" style="left:27px; top:465px;">See how Qorvel Inc is automating thousands of test cases using the platform, and saving thousands of dollars in license fees.</p>

  <h2 class="abs offer-title">WE OFFER :</h2>
  <ul class="abs offer-list">
    <li>
      <svg viewBox="0 0 24 24" fill="none" stroke="var(--teal)" stroke-width="2"><path d="M9 3h6M10 3v6l-5 10a2 2 0 0 0 2 2h10a2 2 0 0 0 2-2l-5-10V3"/><path d="M7 15h10" /></svg>
      Software Testing
    </li>
    <li>
      <svg viewBox="0 0 24 24" fill="none" stroke="var(--teal)" stroke-width="2"><circle cx="12" cy="12" r="9"/><path d="M3 12h18M12 3c3 3 3 15 0 18M12 3c-3 3-3 15 0 18"/></svg>
      Web Development
    </li>
    <li>
      <svg viewBox="0 0 24 24" fill="none" stroke="var(--teal)" stroke-width="2"><rect x="6" y="2" width="12" height="20" rx="2"/><path d="M11 18h2"/></svg>
      App Development
    </li>
  </ul>

  <p class="abs legal">Lorem ipsum dolor sit amet, consectetur adipiscing elit, sed do eiusmod tempor incididunt ut labore et dolore magna aliqua. Ut enim ad minim veniam, quis nostrud exercitation ullamco laboris nisi ut aliquip ex ea commodo consequat. Duis aute irure dolor in reprehenderit in voluptate velit esse cillum dolore eu fugiat nulla pariatur. Excepteur sint occaecat cupidatat non proident.</p>
</section>

<!-- Back page -->
<section class="page back">
  <div class="abs sq" style="left:0; top:0; width:60px; height:47px;"></div>
  <div class="abs sq" style="left:83px; top:27px; width:21px; height:21px;"></div>
  <div class="abs sq" style="left:33px; top:60px; width:44px; height:47px;"></div>

  <h2 class="abs profile-title">VELOCITY<br>BRIGHTLANE</h2>
  <p class="abs profile-text">is a quality assurance centric platform and solution provider that empowers testers and developers to easily create, run, and manage manual and automated tests.</p>

  <div class="abs facts">
    <h3 class="fact-head">Our <span>Vision:</span></h3>
    <p class="fact-text">To focus on creating solutions that deliver mobility, freedom and control via automation and to deliver services which will open new avenues for our customers and allow them to work effectively and creatively.</p>
    <h3 class="fact-head">Our <span>Mission:</span></h3>
    <p class="fact-text">To create a cost effective and easy to use test automation platform that empowers developers and testers in delivering the highest quality software.</p>
    <h3 class="fact-head">Our <span>Advantages:</span></h3>
    <p class="fact-text">With over 10 years of experience in the software industry, we have developed cutting-edge software testing technologies and expertise.<br>We provide enterprise software testing solutions along with software development services at significantly lower cost.</p>
  </div>

  <h3 class="abs section-head" style="top:353px;">Why choose <span>us</span> ?</h3>

  <div class="abs stats">
    <div class="stat">
      <svg viewBox="0 0 40 40" fill="none" stroke="var(--teal)" stroke-width="2.5"><path d="M6 14l3-9h22l3 9z"/><path d="M6 14c0 3 5 3 5 0 0 3 6 3 6 0 0 3 6 3 6 0 0 3 6 3 6 0 0 3 5 3 5 0"/><path d="M8 18v17h24V18"/><rect x="16" y="24" width="8" height="11"/></svg>
      <div class="stat-num">365</div><div class="stat-bar"></div>
      <div class="stat-label">Days open</div>
    </div>
    <div class="stat">
      <svg viewBox="0 0 40 40"><polygon fill="var(--teal)" points="20,2 24,8 31,6 31,13 38,16 33,21 37,27 30,29 29,36 22,33 20,39 18,33 11,36 10,29 3,27 7,21 2,16 9,13 9,6 16,8"/></svg>
      <div class="stat-num">47</div><div class="stat-bar"></div>
      <div class="stat-label">Years of<br>experience</div>
    </div>
    <div class="stat">
      <svg viewBox="0 0 40 40" fill="none" stroke="var(--teal)" stroke-width="2.5"><path d="M9 3h15l8 8v26H9z"/><path d="M24 3v8h8"/></svg>
      <div class="stat-num">35897</div><div class="stat-bar"></div>
      <div class="stat-label">KBs of files</div>
    </div>
    <div class="stat">
      <svg viewBox="0 0 40 40"><circle cx="20" cy="20" r="17" fill="var(--teal)"/><path d="M11 10c4 1 6 4 4 7s2 5 0 8-4 2-5 0M24 7c-2 3 1 5 4 5s4 4 2 7-3 6-5 9" fill="none" stroke="#fff" stroke-width="2.5"/></svg>
      <div class="stat-num">14</div><div class="stat-bar"></div>
      <div class="stat-label">Countries<br>serving</div>
    </div>
  </div>

  <h3 class="abs section-head" style="top:543px;">Our <span>Clients</span></h3>
  <div class="abs clients">
    <span class="client"><i></i>Norvane</span>
    <span class="client"><i></i>Halbrook</span>
    <span class="client"><i></i>Keyloft</span>
    <span class="client"><i></i>Prismat</span>
    <span class="client"><i></i>Webtide</span>
    <span class="client"><i></i>Fastlyne</span>
  </div>

  <div class="abs contact-band">
    <span class="contact-item" style="left:60px;">
      <svg viewBox="0 0 24 24" fill="none" stroke="#fff" stroke-width="2"><rect x="2" y="5" width="20" height="14"/><path d="M2 5l10 8 10-8"/></svg>
      info@velocitybrightlane.com
    </span>
    <span class="contact-item" style="left:270px;">
      <svg viewBox="0 0 24 24" fill="#fff"><path d="M6.6 10.8a15 15 0 0 0 6.6 6.6l2.2-2.2a1 1 0 0 1 1-.25 11.4 11.4 0 0 0 3.6.6 1 1 0 0 1 1 1V20a1 1 0 0 1-1 1A17 17 0 0 1 3 4a1 1 0 0 1 1-1h3.5a1 1 0 0 1 1 1 11.4 11.4 0 0 0 .6 3.6 1 1 0 0 1-.25 1z"/></svg>
      1-888-555-0147
    </span>
  </div>
</section>

</body>
</html>
```